Print Ad for a Human Resource Company

Hi.
Apologies for the quick turnaround but I just was brought on board to handle this project. The publication is Coral Ridge Quarterly, a Hawaii Business & Lifestyle publication.
Their upcoming issue will feature HR companies & of course we want our ad to stand out from the rest & make the phone ring.

Size: Vertical Ad 2.5" x 9.875

Color: 4 color, non bleed

Format: Hi-res (300 dpi) pdf
Ad Due: Drop dead dealine is Friday, 1/04/2013

Color: 4 color, non bleed

Reason: There is a God in heaven. We have a stay on the deadline to January 4th.

Target Market(s)

Small companies that benefit from having experts handle these areas.

Industry/Entity Type

Business

Requirements
Must have
• Copy:
Tagline: Keeping It Simple
Accounting
Human Resources
Payroll Services
Employee Benefits
Commercial Insurance
Personal Insurance
No Hidden Fees

Photos of both owners:
Marisela Kahoku, CEO
Tina Borwick, President

Company logo
Address: 512 Lumber Mill Service Road, Suite #204
Honolulu, HI 96819
Phone: 808.555.0173
BrightLedgerAid.example
Nice to have
• This is a small locally owned firm owned by 2 local, very smart, sophisticated yet approachable, hardworking women. Their colors are Black background, silver type. The ad should be a reflection of their personalities.

```html
<!DOCTYPE html>
<html lang="en">
<head>
<meta charset="utf-8">
<title>BrightLedger – Coral Ridge Quarterly Ad</title>
<link rel="stylesheet" href="https://fonts.googleapis.com/css2?family=Nunito+Sans:wght@300;700;800&family=Crimson+Text:wght@400&display=swap">
<style>
  :root {
    --page: #ffffff;
    --ad-black: #000000;
    --type-white: #ffffff;
    --type-silver: #e6e6e6;
    --tag-red: #e0141a;
    --frame-light: #d9d9d9;
    --frame-dark: #6b6b6b;
    --glow-grey: #8c8c8c;
  }
  * { box-sizing: border-box; margin: 0; padding: 0; }
  html, body {
    width: 1000px; height: 1200px; overflow: hidden;
    background: var(--page);
    font-family: "Nunito Sans", Arial, sans-serif;
  }
  .ad {
    position: absolute; left: 358px; top: 0;
    width: 303px; height: 1198px;
    background: var(--ad-black);
    border: 1px solid #333;
    color: var(--type-white);
    overflow: hidden;
  }
  .brand {
    position: absolute; top: 26px; left: 0; width: 100%;
    text-align: center;
    font-weight: 800; font-size: 34px; letter-spacing: 1px;
    color: var(--type-white);
    white-space: nowrap;
  }
  .services {
    position: absolute; top: 128px; left: 36px;
    list-style: none;
  }
  .services li {
    position: relative;
    padding-left: 20px;
    font-weight: 700; font-size: 19.5px; line-height: 31px;
    white-space: nowrap;
  }
  .services li::before {
    content: ""; position: absolute; left: 0; top: 13px;
    width: 6px; height: 6px; border-radius: 50%;
    background: var(--type-white);
  }
  .team {
    position: absolute; left: 1px; top: 358px;
    width: 301px; height: 522px;
  }
  .glow {
    position: absolute;
    background: radial-gradient(ellipse at center, var(--glow-grey) 0%, #3a3a3a 55%, #000 100%);
  }
  .glow.upper { left: 0; top: 0; width: 301px; height: 260px; }
  .glow.lower { left: 0; top: 260px; width: 301px; height: 262px; }
  .portrait-frame {
    position: absolute;
    background: linear-gradient(135deg, var(--frame-light), var(--frame-dark) 50%, var(--frame-light));
    padding: 3px;
  }
  .portrait-inner {
    width: 100%; height: 100%;
    background: #000;
    position: relative;
  }
  .portrait-photo {
    position: absolute; left: 7px; top: 6px; right: 7px;
    background: radial-gradient(ellipse at 50% 35%, #cfcfcf 0%, #8a8a8a 45%, #222 85%);
  }
  .portrait-caption {
    position: absolute; left: 0; right: 0; bottom: 8px;
    text-align: center;
    font-weight: 700; font-size: 14px;
    color: var(--type-white);
    white-space: nowrap;
  }
  .portrait-frame.president { left: 12px; top: 4px; width: 198px; height: 258px; }
  .portrait-frame.president .portrait-photo { height: 211px; }
  .portrait-frame.ceo { left: 85px; top: 262px; width: 200px; height: 260px; }
  .portrait-frame.ceo .portrait-photo { height: 213px; }
  .tagline {
    position: absolute; top: 914px; left: 0; width: 100%;
    text-align: center;
    font-family: "Crimson Text", Georgia, serif;
    font-size: 40px; line-height: 48px; color: var(--tag-red);
    white-space: nowrap;
    letter-spacing: -0.8px;
    transform: rotate(-6deg);
    transform-origin: 50% 50%;
  }
  .address {
    position: absolute; top: 1008px; left: 0; width: 100%;
    text-align: center;
    font-weight: 300; font-size: 17.5px; line-height: 20px;
    color: var(--type-silver);
    white-space: nowrap;
  }
  .phone {
    position: absolute; top: 1106px; left: 0; width: 100%;
    display: flex; justify-content: center; align-items: center; gap: 5px;
    font-weight: 700; font-size: 17px;
  }
  .web {
    position: absolute; top: 1148px; left: 0; width: 100%;
    text-align: center;
    font-weight: 700; font-size: 16.5px;
    white-space: nowrap;
  }
</style>
</head>
<body>
<div class="ad">
  <div class="brand">BRIGHTLEDGER</div>

  <ul class="services">
    <li>Accounting</li>
    <li>Human Resources</li>
    <li>Payroll Services</li>
    <li>Employee Benefits</li>
    <li>Commercial Insurance</li>
    <li>Personal Insurance</li>
    <li>No Hidden Fees</li>
  </ul>

  <div class="team">
    <div class="glow upper"></div>
    <div class="glow lower"></div>
    <div class="portrait-frame president">
      <div class="portrait-inner">
        <div class="portrait-photo" role="img" aria-label="Portrait photo of Tina Borwick, President, in a black top against a grey studio backdrop"></div>
        <div class="portrait-caption">Tina Borwick, President</div>
      </div>
    </div>
    <div class="portrait-frame ceo">
      <div class="portrait-inner">
        <div class="portrait-photo" role="img" aria-label="Portrait photo of Marisela Kahoku, CEO, in a black top against a grey studio backdrop"></div>
        <div class="portrait-caption">Marisela Kahoku, CEO</div>
      </div>
    </div>
  </div>

  <div class="tagline">Keeping It Simple</div>

  <div class="address">
    Address:<br>
    512 Lumber Mill Service Road,<br>
    Suite #204<br>
    Honolulu, HI 96819
  </div>

  <div class="phone">
    <svg width="18" height="18" viewBox="0 0 18 18" aria-hidden="true">
      <circle cx="9" cy="9" r="8" fill="none" stroke="#fff" stroke-width="1"/>
      <path d="M6 4.5 L7.5 4.5 L8 6.8 L7 7.6 Q7.8 9.6 10.2 11 L11 10 L13.3 10.6 L13.3 12 Q12.5 13.4 10.8 13 Q6.2 11.4 4.8 7 Q4.6 5.2 6 4.5 Z" fill="#fff"/>
    </svg>
    <span>808 555 0173</span>
  </div>

  <div class="web">www.BrightLedgerAid.example</div>
</div>
</body>
</html>
```